Flyer Advertisement Simple But Creative

Flyer dimensions 4" x 6"

Simple design with logo and additional info. On the front of the flyer:

- place the logo at the top
- beneath the logo add the website and phone number
- simple less is more approach
- feel free to add your own personal touch

On the back:

- Requirements
- Perfect for Birthdays and Anniversaries
- Rentals available hourly, daily, and weekly
- Group Rentals available at discounted rates
- Enter to win a free rental - url and QR code

Industry/Entity Type

Car Rental

Font styles to use
Serif
Sans Serif

Colors

Designer to choose colors to be used in the design.

Requirements
Must have
• FRONT:
• Please include our phone number and website:
• 832-519-2086
• www.BrazosTrikeHire.com
• BACK:
• REQUIREMENTS
• At least 25 years of age
• Valid Driver's License
• Debit or Credit Card
• Must know how to drive a manual transmission or stick shift

```html
<!DOCTYPE html>
<html lang="en">
<head>
<meta charset="utf-8">
<title>Brazos Trike Hire – Flyer</title>
<link href="https://fonts.googleapis.com/css2?family=Fira+Sans+Condensed:wght@400;500;600;700&display=swap" rel="stylesheet">
<style>
  :root{
    --backdrop:#2b2b2b;
    --card-light:#f6f6f6;
    --card-mid:#dcdcdc;
    --ink:#1c1414;
    --ink-soft:#2a2222;
    --red:#c4141c;
    --red-deep:#7a0c10;
    --white:#ffffff;
    --photo-red:#b51a22;
    --photo-grey:#8c8984;
  }
  *{margin:0;padding:0;box-sizing:border-box}
  html,body{width:815px;height:1200px;overflow:hidden;background:var(--backdrop)}
  .flyer-side{
    position:absolute;left:112px;width:591px;height:415px;overflow:hidden;
    background:linear-gradient(180deg,var(--card-light) 0%,var(--card-mid) 100%);
    font-family:"Fira Sans Condensed",sans-serif;color:var(--ink);
  }
  .flyer-front{top:145px}
  .flyer-back{top:649px}

  /* front */
  .logo-art{
    position:absolute;left:34px;top:14px;width:190px;height:172px;border-radius:50%;
    background:radial-gradient(circle at 50% 45%,#d8dadd 0%,#bfc3c7 55%,rgba(200,203,206,0) 72%);
  }
  .brand-name{
    position:absolute;left:0;top:194px;width:258px;text-align:center;white-space:nowrap;
    font-family:"Fira Sans Condensed",sans-serif;font-weight:700;font-size:21px;
    letter-spacing:1px;color:var(--ink);text-transform:uppercase;line-height:26px;
  }
  .brand-name::before{
    content:"";display:inline-block;width:9px;height:9px;background:var(--red);
    margin-right:7px;vertical-align:2px;
  }
  .front-photo{
    position:absolute;left:248px;top:0;width:343px;height:415px;
    background:linear-gradient(135deg,#b7b3ad 0%,var(--photo-grey) 30%,var(--photo-red) 55%,#6e0f14 80%,#2a2424 100%);
    clip-path:polygon(18% 0,100% 0,100% 100%,20% 100%,12% 88%,4% 72%,0 55%,3% 40%,1% 28%,8% 16%,12% 8%);
  }

  .phone-band{
    position:absolute;height:46px;display:flex;align-items:center;justify-content:center;gap:4px;
    background:var(--ink);color:var(--white);white-space:nowrap;
    font-weight:600;font-size:19px;letter-spacing:.5px;
    clip-path:polygon(3% 12%,97% 0,100% 40%,96% 88%,6% 100%,0 60%);
  }
  .phone-band svg{width:22px;height:22px;flex:none}
  .web-pill{
    position:absolute;height:25px;border-radius:13px;display:flex;align-items:center;justify-content:center;
    background:linear-gradient(90deg,var(--ink) 0%,var(--ink-soft) 60%,var(--red-deep) 100%);
    color:var(--white);font-weight:600;font-size:12.5px;letter-spacing:.4px;white-space:nowrap;
    box-shadow:0 4px 6px rgba(0,0,0,.3);
  }
  .flyer-front .phone-band{left:12px;top:275px;width:236px}
  .flyer-front .web-pill{left:10px;top:348px;width:245px}

  /* back */
  .back-photo{
    position:absolute;left:0;top:0;width:330px;height:330px;
    background:linear-gradient(150deg,#cfcfcf 0%,#5a5a5a 25%,#2c2a2a 50%,var(--photo-red) 70%,#3a3838 100%);
    clip-path:polygon(0 0,100% 0,96% 40%,85% 68%,68% 88%,45% 100%,0 100%);
  }
  .req-title{
    position:absolute;left:342px;top:58px;width:249px;white-space:nowrap;
    font-family:"Fira Sans Condensed",sans-serif;font-weight:500;font-size:33px;letter-spacing:.3px;line-height:44px;
    border-bottom:2px solid var(--red-deep);
  }
  .req-title .initial{color:var(--red)}
  .req-item{
    position:absolute;background:var(--ink);color:var(--white);
    display:flex;align-items:center;padding:0 8px;line-height:1;white-space:nowrap;
  }
  .req-item .big{font-weight:700;font-size:21px}
  .req-item .small{font-weight:400;font-size:13px;margin:0 4px}
  .req-age{left:331px;top:132px;height:31px}
  .req-license{left:383px;top:162px;height:45px}
  .req-license .big{font-size:25px}
  .req-card{left:316px;top:205px;height:30px}
  .req-manual{left:268px;top:237px;width:311px;height:70px;flex-direction:column;align-items:flex-start;justify-content:center;padding:0 12px}
  .req-manual .row{display:flex;align-items:baseline;gap:5px}
  .req-manual .mid{font-weight:600;font-size:18px;letter-spacing:1px}
  .req-manual .huge{font-weight:700;font-size:27px;letter-spacing:1px}
  .flyer-back .phone-band{left:160px;top:318px;width:234px}
  .flyer-back .web-pill{left:163px;top:378px;width:244px}
</style>
</head>
<body>

<section class="flyer-side flyer-front">
  <div class="logo-art" role="img" aria-label="Sketched illustration of a red three-wheeled roadster over a grey brush swirl"></div>
  <div class="brand-name">Brazos Trike Hire</div>
  <div class="phone-band">
    <svg viewBox="0 0 24 24" aria-hidden="true"><circle cx="12" cy="12" r="10.5" fill="none" stroke="#fff" stroke-width="1.8"/><path d="M8.6 6.8c.4-.4 1-.4 1.3 0l1.3 1.7c.3.4.2.9-.1 1.2l-.8.8c.6 1.4 1.7 2.5 3.1 3.1l.8-.8c.3-.3.8-.4 1.2-.1l1.7 1.3c.4.3.4.9 0 1.3l-.9.9c-.6.6-1.5.8-2.3.4-2.7-1.2-4.8-3.3-6-6-.4-.8-.2-1.7.4-2.3z" fill="#fff"/></svg>
    <span>832-519-2086</span>
  </div>
  <div class="web-pill">www.BrazosTrikeHire.com</div>
  <div class="front-photo" role="img" aria-label="Photo of the front end of a glossy red three-wheeled roadster on pavement"></div>
</section>

<section class="flyer-side flyer-back">
  <div class="back-photo" role="img" aria-label="Photo of the roadster cockpit with steering wheel, gauges, screen and gear shifter"></div>
  <h2 class="req-title"><span class="initial">R</span>EQUIREMENTS</h2>
  <div class="req-item req-age"><span class="big">At least 25</span><span class="small">years of age</span></div>
  <div class="req-item req-license"><span class="small">Valid Driver's</span><span class="big">License</span></div>
  <div class="req-item req-card"><span class="big">Debit</span><span class="small">or Credit Card</span></div>
  <div class="req-item req-manual">
    <div class="row"><span class="small">Must know how to</span><span class="mid">drive a manual</span></div>
    <div class="row"><span class="small">transmission</span><span class="huge">or stick shift</span></div>
  </div>
  <div class="phone-band">
    <svg viewBox="0 0 24 24" aria-hidden="true"><circle cx="12" cy="12" r="10.5" fill="none" stroke="#fff" stroke-width="1.8"/><path d="M8.6 6.8c.4-.4 1-.4 1.3 0l1.3 1.7c.3.4.2.9-.1 1.2l-.8.8c.6 1.4 1.7 2.5 3.1 3.1l.8-.8c.3-.3.8-.4 1.2-.1l1.7 1.3c.4.3.4.9 0 1.3l-.9.9c-.6.6-1.5.8-2.3.4-2.7-1.2-4.8-3.3-6-6-.4-.8-.2-1.7.4-2.3z" fill="#fff"/></svg>
    <span>832-519-2086</span>
  </div>
  <div class="web-pill">www.BrazosTrikeHire.com</div>
</section>

</body>
</html>
```